Accounting firm needs a flyer "TORV Group".. many job after this Stationary, business card

We need a flyer for a new company based in Melbourne Australia. We are group of young professionals who intend to provide various accounting services, taxation, finance, bookkeeping and payroll, Business service service advisory and management consulting.The main task of the firm is to provide accounting and taxation services. we then use our associates/referral partners to assist client with their legal, migration, finance needs.

We would like to see designs that match our logo, business card and letter head which I have uploaded along with this. I have also uploaded some of our website contents that might be used in flyers.
My favorite colors are: Blue (navy and royal blue), Teal (blue green), Turquoise, purple(orchid, lavender, plum).

Our brand:
TORV Group
Where advice mean more

Our mission:
To group the professionals in house, where advice mean more and turn into better business for our people, for our clients and four our communities.

We like our logo, however we are still not sure about our business card. So if we are open to work with someone who works with flyers and business card at the same time .

Target Market(s)

Individual and business client in Australia

Industry/Entity Type

Finance And Accounting

Colors
0255a3
3176b5
0493ce
33a6d7
886aae
b768aa
00a990
33b8a4

Requirements
Must have
• TORV Group logo
• Liability limited by a scheme approved under the professional standards legislation
• Our motto: TORV Group, clarity that builds value
• Short description of our services:
• • Bookkeeping & Payroll
• • Finance & Capital Raising
• • Taxation, Accounting and compliances
• • Business service and advisory
• • Migration
• • NBRE and Corporate Secretarial
• • Business law and legal services
• About us
• TORV aim to be more than just an accounting firm. We support our clients to help them achieve their personal and business goals by offering a fully integrated advisory service, helping clients to build wealth and protect their assets.We will bring together the relevant professionals across a number of specialties and locations; providing a responsive, personalised solution.
• Our mission: To group the professionals in house, where advice mean more and turn into better business for our people, for our clients and four our communities.
Nice to have
• Tax agent logo
• OFW logo

```html
<!DOCTYPE html>
<html lang="en">
<head>
<meta charset="utf-8">
<title>TORV Group flyer</title>
<link rel="stylesheet" href="https://fonts.googleapis.com/css2?family=Oswald:wght@500&family=Open+Sans:wght@400;600;700&display=swap">
<style>
:root{
  --navy:#0255a3;
  --royal:#3176b5;
  --cyan:#0493ce;
  --sky:#33a6d7;
  --ink:#222;
  --stage:#2e2e2e;
  --grey:#c9ccd2;
}
*{margin:0;padding:0;box-sizing:border-box}
html,body{width:1200px;height:1200px;overflow:hidden;background:var(--stage);font-family:"Open Sans",sans-serif;color:var(--ink)}
.sheet{position:absolute;top:214px;width:508px;height:713px;background:#fff;overflow:hidden;box-shadow:0 4px 14px rgba(0,0,0,.45)}
.sheet--front{left:59px}
.sheet--back{left:616px}

/* front */
.hero-photo{position:absolute;left:0;top:0;width:508px;height:240px;background:linear-gradient(180deg,#dfe2e7,#eef0f3 70%,#f6f7f9)}
.hero-wave{position:absolute;left:0;top:130px}
.brand-mark{position:absolute;left:424px;top:20px;width:62px;text-align:center}
.brand-mark .disc{width:56px;height:56px;border-radius:50%;background:var(--navy);margin:0 auto 2px}
.brand-mark span{font:700 13px "Open Sans",sans-serif;color:var(--navy)}
.headline{position:absolute;left:40px;top:62px;font-family:"Oswald",sans-serif;font-weight:500;line-height:1.12;letter-spacing:-.5px}
.headline .l1{font-size:42px;color:#1d4a8a}
.headline .l2{font-size:36px;color:var(--cyan)}
.about{position:absolute;left:17px;top:266px;width:476px}
.about h2{font-size:27px;font-weight:400;color:var(--navy);border-bottom:1px solid var(--navy);display:inline-block;line-height:1.1;margin-bottom:8px}
.about h2 b{color:var(--cyan);font-weight:600}
.pill{display:inline-flex;align-items:center;background:var(--navy);color:#fff;font-size:10px;font-weight:600;border-radius:10px;padding:1px 8px 1px 1px;margin:4px 0 3px}
.pill i{width:17px;height:17px;border-radius:50%;background:#fff;border:3px solid var(--sky);margin-right:4px}
.about p{font-size:7.2px;line-height:1.4;margin-bottom:7px;text-align:justify}
.foot-wave{position:absolute;left:0;top:600px}
.contact{position:absolute;font-size:8.4px;font-weight:700;line-height:1.35;display:flex;align-items:center;gap:6px;white-space:nowrap}
.contact svg{flex:none}

/* back */
.col-services{position:absolute;left:0;top:0;width:250px;height:698px;padding:14px 4px 0 16px}
.col-partners{position:absolute;left:250px;top:0;width:258px;height:698px;background:var(--navy);color:#fff;padding:12px 8px 0 12px}
.type-title{font-size:29px;color:var(--navy);font-weight:400;line-height:1.1;border-bottom:1px solid var(--navy);display:inline-block;margin-bottom:6px}
.type-title b{color:var(--cyan);font-weight:600}
.svc{margin-bottom:7px}
.svc h3{display:flex;align-items:center;gap:5px;font-size:9.4px;font-weight:600;text-decoration:underline;color:var(--navy);margin-bottom:6px}
.svc h3 i{width:15px;height:15px;border-radius:50%;background:var(--navy);flex:none}
.col-partners .svc h3{color:#fff}
.col-partners .svc h3 i{background:#fff}
.svc p{font-size:5.6px;line-height:1.4;text-align:justify;margin-bottom:5px}
.ticks{list-style:none;display:grid;grid-template-columns:1fr 1fr;gap:5px 8px;font-size:5.5px;line-height:1.35}
.ticks li{position:relative;padding-left:9px}
.ticks li::before{content:"";position:absolute;left:1px;top:1px;width:4px;height:4px;background:var(--cyan);transform:rotate(45deg)}
.col-partners .ticks li::before{background:#fff}
.back-foot{position:absolute;left:6px;top:660px;width:238px;border-top:1px solid var(--navy);padding-top:6px;display:flex;align-items:center;gap:8px}
.back-foot .name{font-size:11px;color:var(--navy);line-height:1.3;border-right:1px solid var(--navy);padding-right:6px}
.badge{width:24px;height:24px;border-radius:50%;background:var(--grey)}
.web-bar{position:absolute;left:0;top:698px;width:508px;height:15px;background:var(--cyan);color:#fff;font-size:7.5px;font-weight:700;text-align:center;line-height:15px;padding-left:110px}
</style>
</head>
<body>

<section class="sheet sheet--front">
  <div class="hero-photo" role="img" aria-label="Photo of a cheering team of young professionals, softly faded"></div>
  <svg class="hero-wave" width="508" height="140" viewBox="0 0 508 140">
    <path d="M0 75 C150 115 330 90 508 0 L508 30 C360 120 170 150 0 105 Z" fill="var(--cyan)"/>
    <path d="M0 110 C170 150 360 120 508 30 L508 55 C370 140 180 160 0 125 Z" fill="var(--navy)"/>
    <path d="M40 140 C200 135 380 110 508 60 L508 70 C380 130 220 145 40 140 Z" fill="var(--grey)"/>
  </svg>
  <div class="brand-mark"><div class="disc"></div><span>TORV</span></div>
  <div class="headline"><div class="l1">TORV GROUP,</div><div class="l2">clarity that builds value</div></div>

  <div class="about">
    <h2><b>About</b> us</h2><br>
    <span class="pill"><i></i>Our mission</span>
    <p>To group the professionals in house, where advice mean more and turn into better business for our people, for our clients and four our communities.</p>
    <span class="pill"><i></i>Our firm</span>
    <p>As a group of professionals, our firm are available to provide you with high quality accounting, taxation and business advisory whether you are a business owner, family or an individual client. We have a strategic alliance with our referral lawyers, migration agents and mortgage brokers.</p>
    <p>TORV believe the first step to any engagement is understanding ‘you’. This is because every business is unique and every business owner has different needs. You know your business better than anyone so we want to hear it from you. We will then work with you to tailor our advisory offering to your needs. We will bring together the relevant professionals across a number of specialities and locations; providing a responsive, personalised solution.</p>
    <p>We take a whole of life approach because we know that when you’re running a business not all costs are financial – you might just want to work fewer hours. And that is why we are different.</p>
    <p>We aim to be more than just an accounting firm. We support our clients to help them achieve their personal and business goals by offering a fully integrated advisory service, helping clients to build wealth and protect their assets.</p>
    <p>Our core values include expertise, confidentiality, teamwork and commitment.</p>
    <span class="pill"><i></i>Work with us</span>
    <p>At TORV Group we are dealing with variety of professionals. Whether you’re a graduate ready to begin your career or an experienced professional, contact us via email if you believe you have what it takes to help businesses recover from financial challenges.</p>
  </div>

  <svg class="foot-wave" width="508" height="113" viewBox="0 0 508 113">
    <path d="M0 40 C150 -5 330 10 508 60 L508 75 C330 30 150 20 0 55 Z" fill="var(--grey)"/>
    <path d="M0 20 C160 -10 340 10 508 96 L508 113 L478 113 C350 40 160 30 0 60 Z" fill="var(--navy)"/>
    <path d="M0 60 C160 30 350 40 478 113 L0 113 Z" fill="#fff"/>
  </svg>
  <div class="contact" style="left:26px;top:678px">
    <svg width="12" height="15" viewBox="0 0 12 15"><path d="M6 0a6 6 0 0 1 6 6c0 4-6 9-6 9S0 10 0 6a6 6 0 0 1 6-6z" fill="#111"/><circle cx="6" cy="6" r="2.2" fill="#fff"/></svg>
    <span>Level 5, 88 Harbour Lane<br>MELBOURNE VIC 3000</span>
  </div>
  <div class="contact" style="left:186px;top:672px">
    <svg width="12" height="12" viewBox="0 0 12 12"><path d="M2 0l3 3-1.5 2a8 8 0 0 0 3.5 3.5L9 7l3 3-2 2C5 12 0 7 0 2z" fill="#111"/></svg>
    <span>0400 000 123</span>
  </div>
  <div class="contact" style="left:186px;top:690px">
    <svg width="12" height="9" viewBox="0 0 12 9"><rect x=".5" y=".5" width="11" height="8" fill="none" stroke="#111"/><path d="M.5 .5l5.5 4.5 5.5-4.5" fill="none" stroke="#111"/></svg>
    <span>hi@torv.example</span>
  </div>
  <div class="contact" style="left:300px;top:690px">
    <svg width="10" height="10" viewBox="0 0 10 10"><circle cx="5" cy="5" r="4.5" fill="none" stroke="#111"/><path d="M.5 5h9M5 .5c-3 3-3 6 0 9M5 .5c3 3 3 6 0 9" fill="none" stroke="#111" stroke-width=".8"/></svg>
    <span>www.torv.example</span>
  </div>
</section>

<section class="sheet sheet--back">
  <div class="col-services">
    <h2 class="type-title"><b>Type</b> of services:</h2>

    <div class="svc">
      <h3><i></i>Taxation, Accounting and compliances</h3>
      <p>At TORV experienced tax agent build close working relationships with you to understand your circumstances and develop customised solutions for your personal income tax and corporate tax exposure. The consultative approach combined with extensive industry experience allows us to deliver practical and relevant tax minimisation services and advice.</p>
      <ul class="ticks"><li>Tax returns for all structures</li><li>Capital gain tax</li><li>Amendments to tax returns</li><li>Tax planning</li><li>FBT Returns</li><li>Quarterly or monthly Activity Statements</li><li>Tax Office liaison</li><li>Tax Office Audits</li></ul>
    </div>

    <div class="svc">
      <h3><i></i>Business service and advisory</h3>
      <p>While we provide peace of mind though taking care of the usual accounting and tax compliance matters, our real value lies in seeking to help you address business challenges and uncover opportunities. TORV do this by developing a deep understanding of your needs, challenges and ambitions. We will then work with you to tailor our advisory offering to your needs. TORV advice will be designed to ensure you get the attention you need… when you need it.</p>
      <ul class="ticks"><li>Business registrations</li><li>Business planning</li><li>Business purchase and due diligence</li><li>Strategic business advice &amp; planning</li><li>Business Sale</li><li>Proposals for cash-flow improvement</li><li>Restructures &amp; Asset protection</li></ul>
    </div>

    <div class="svc">
      <h3><i></i>Book keeping &amp; Payroll</h3>
      <p>Do you really want to waste time crunching the numbers and completing your bookwork when you could be spending that time on your business? Our bookkeeping involves maintaining accurate and updated records of all your business and personal financial activities. We manage your payroll on an ongoing basis, ensuring that all employees are compensated according to their employment agreements.</p>
      <ul class="ticks"><li>Cloud accounting system for small business</li><li>Work cover reporting</li><li>Cloud ledger platforms</li><li>GST, PAYG and BAS report</li><li>Payroll system</li><li>Financial reports</li><li>Payroll tax and annual State Revenue lodgements</li><li>Inter-entity loan</li></ul>
    </div>

    <div class="svc">
      <h3><i></i>Finance &amp; Capital Raising</h3>
      <p>Need a second opinion? Want a better loan? Talk with TORV today.</p>
      <p>We regularly review client portfolios to identify opportunities and refer them to experienced and professional finance brokers to save and assist them with renegotiating a better deal with their current lender or seek out a better loan from a different lender.</p>
      <p>TORV ensure that our mortgage brokers have all financial information at hand and that it is clearly understood. This enables you to have a far greater opportunity for approval, securing the most appropriate finance structure, low rate/fees and product for your situation.</p>
      <ul class="ticks"><li>Owner occupier home loans for first home buyers</li><li>Finance for property renovators and developers</li><li>Loans for property investors</li><li>Re-financing for a better deal</li><li>Business loans</li><li>All of your motor vehicle, plant &amp; equipment needs</li></ul>
    </div>

    <div class="back-foot">
      <span class="name">TORV Tax and<br>Business Advisors</span>
      <span style="display:flex;align-items:center;gap:3px;font-size:8px;font-weight:700;color:var(--navy)"><span class="badge" style="background:var(--sky)"></span>OFW</span>
      <span class="badge" style="margin-left:40px"></span>
    </div>
  </div>

  <div class="col-partners">
    <div class="svc">
      <h3><i></i>NBRE and Corporate Secretarial</h3>
      <p>TORV understand that your corporate register, minutes and officeholder information and other secretarial register must kept for the life of the entity. Therefore, we maintain these documents. We will also update all registers when there is any change of details.</p>
      <ul class="ticks"><li>Company searches and information retrieval</li><li>Preparation of Minutes and Resolutions</li><li>Maintenance of company registers</li><li>Changes to officeholders/addresses</li><li>Share transfers</li><li>Attendance to all other statutory requirements</li></ul>
    </div>
    <div class="svc">
      <h3><i></i>Migration</h3>
      <p>The business Innovation visa or Employer Business Sponsored visa application can be complex with the requirement to submit various business, financial and asset documents. We can assist business of all sizes to ensure the case for application is clear to the Home Affairs assessment officer. TORV work with highly professional migration agents &amp; lawyers. Our goal is to secure your Australian visa in the quickest time and with the minimum fuss.</p>
      <ul class="ticks"><li>Business set up</li><li>Sourcing for Australian business to be purchased for the purposes of the visa</li><li>Business plan for migration</li><li>Looking for real estate – an office for your business or home for your family</li><li>Liaising with migration agents and Home Affairs</li><li>Referring logistics companies to move personal effects or business equipment</li><li>Strategic business advisory for best chance of approval</li></ul>
    </div>
    <div class="svc">
      <h3><i></i>Insolvency &amp; Restructuring</h3>
      <p>TORV emphasis is on providing quality and timely analysis, advice and solutions to businesses facing financial difficulties. We believe that ideal solution for clients is turnaround and restructuring solution, but remains aware that, in certain circumstances, the best outcome is to implement formal insolvency proceedings to minimise any adverse financial impact on stakeholders. We ensure that our clients get access to:</p>
      <ul class="ticks"><li>Highly skilled specialists who bring innovative and practical solutions</li><li>A trusted advisor that is cost-effective and outcomes focused</li><li>Specialists with a proven track record in facilitating restructuring outcomes</li><li>Thorough investigative capabilities</li></ul>
    </div>
    <div class="svc">
      <h3><i></i>Management Consulting Services</h3>
      <p>Irrespective of the size of your business, TORV can implement management accounting procedures to ensure a flow of regular, meaningful financial reports. TORV advice is designed to provide a springboard for further action. We review the reports and discuss the strategic options for the future of your business.</p>
      <ul class="ticks"><li>Business and Strategic Planning</li><li>Costing &amp; Pricing Strategies</li><li>Growth and Profit Strategies</li><li>Benchmarking and KPI’s</li><li>Budgets, Forecasts and Cash Flow Projections</li><li>Succession Planning</li><li>Management Reporting</li><li>Practical Business Advice</li><li>Financial Analysis</li></ul>
    </div>
    <div class="svc">
      <h3><i></i>Business law and legal services</h3>
      <p>When it comes to business law and legal services, you want to ensure you have a trusted competent legal team to work alongside with your accountants to help you across the broad range of commercial circumstances. At TORV, we have strategic alliance with various law firms where they have extensive expertise across various areas. Whether you need to draft contracts for employees, prepare your business for sale, are considering buying a business or if you have a court matter, we work alongside with lawyers to you smooth out the process and help deliver a favourable outcome to you.</p>
      <ul class="ticks"><li>Business purchase</li><li>Contract review</li><li>Business sale</li><li>Conveyancing</li><li>Business structure</li></ul>
    </div>
  </div>

  <div class="web-bar">www.torv.example</div>
</section>

</body>
</html>
```